Home Design company focused on remodel and enhancement of kitchens and bathroorms

I already have a logo designed by ArtHive, I now need a design for my business cards.
The company is in the remodeling and enhancement industry for homes, focusing on kitchens and bathrooms, however, we can remodel or enhance every room in a home, an office space, etc.

The company's name is VORNETT HOME DESIGN, LLC

We'll focus on clients in the Rio Grande Valley, Texas. Primarily McAllen, Edinburg, Pharr, Mission, Brownsville and South Padre Island.

The design on the business card should transmit reliability, professionalism anda bit of upscale design.

The logo is in black and white, and would like to keep it that way.

The information that needs to be printed in the business cards is:
Company's name: Vornett Home Design
My name: Mira Lindqvist
Address, phone and email:
2715 N Parkline Rd, Ste 318
Alderwick, OR 70913
(555) 731 2958
mlindqvist@vornettstudio.com
Website: vornettstudio.com

```html
<!DOCTYPE html>
<html lang="en">
<head>
<meta charset="utf-8">
<title>Vornett Home Design — Business Card</title>
<link href="https://fonts.googleapis.com/css2?family=Montserrat:wght@400&family=Arimo:wght@400;700&display=swap" rel="stylesheet">
<style>
  :root {
    --stage: #1b1b1c;
    --card-light: #f7f7f5;
    --card-dark: #1f1f21;
    --ink: #141414;
    --ink-soft: #8a8a8a;
    --rule: #555555;
    --paper-text: #ffffff;
    --mark-tone: #2a2a2c;
  }
  * { margin: 0; padding: 0; box-sizing: border-box; }
  html, body { width: 1200px; height: 963px; overflow: hidden; }
  body {
    background: var(--stage);
    display: flex;
    align-items: center;
    justify-content: center;
    gap: 60px;
  }
  .card {
    width: 520px;
    height: 297px;
    position: relative;
    overflow: hidden;
  }

  /* Front */
  .card--front { background: var(--card-light); color: var(--ink); }
  .wordmark {
    position: absolute;
    top: 62px;
    left: 0; right: 0;
    display: flex;
    justify-content: center;
    align-items: center;
    gap: 16px;
  }
  .wordmark__square {
    width: 46px; height: 46px;
    border: 2px solid var(--ink);
  }
  .wordmark__rule { width: 1px; height: 66px; background: var(--ink); }
  .wordmark__name {
    font-family: "Montserrat", sans-serif;
    font-weight: 400;
    font-size: 17px;
    line-height: 1.12;
    letter-spacing: 0.34em;
    text-transform: uppercase;
  }
  .details {
    position: absolute;
    left: 0; right: 0;
    bottom: 48px;
    display: flex;
    justify-content: center;
    align-items: stretch;
    gap: 18px;
    font-family: "Arimo", sans-serif;
  }
  .details__who { text-align: right; padding-top: 2px; }
  .details__name {
    font-weight: 700;
    font-size: 13px;
    letter-spacing: 0.03em;
    text-transform: uppercase;
    margin-bottom: 3px;
  }
  .details__address { font-size: 11px; line-height: 1.35; color: var(--ink-soft); }
  .details__rule { width: 1px; background: var(--rule); }
  .contact { list-style: none; padding-top: 20px; }
  .contact li {
    display: flex;
    align-items: center;
    gap: 8px;
    font-size: 11px;
    line-height: 1.4;
    color: var(--ink-soft);
  }
  .contact svg { width: 10px; height: 10px; flex: none; }

  /* Back */
  .card--back { background: var(--card-dark); }
  .back__name {
    position: absolute;
    top: 28px; left: 30px;
    font-family: "Montserrat", sans-serif;
    font-weight: 400;
    font-size: 22px;
    letter-spacing: 0.3em;
    color: var(--paper-text);
    text-transform: uppercase;
    white-space: nowrap;
  }
  .back__field {
    position: absolute;
    left: 30px; right: 30px;
    top: 84px; bottom: 0;
    background: linear-gradient(160deg, var(--mark-tone), var(--card-dark));
  }
</style>
</head>
<body>

<section class="card card--front" aria-label="Card front">
  <div class="wordmark">
    <div class="wordmark__square"></div>
    <div class="wordmark__rule"></div>
    <div class="wordmark__name">Vornett<br>Home<br>Design</div>
  </div>

  <div class="details">
    <div class="details__who">
      <p class="details__name">Mira Lindqvist</p>
      <p class="details__address">2715 N Parkline Rd<br>Ste 318, Alderwick, OR 70913</p>
    </div>
    <div class="details__rule"></div>
    <ul class="contact">
      <li>
        <svg viewBox="0 0 10 10" aria-hidden="true"><path d="M2 0.5 L3.6 2.6 L2.7 3.6 Q3.8 6 6.4 7.3 L7.4 6.4 L9.5 8 L8.3 9.5 Q2.5 8.5 0.5 1.7 Z" fill="#141414"/></svg>
        (555) 731 2958
      </li>
      <li>
        <svg viewBox="0 0 10 10" aria-hidden="true"><rect x="0.6" y="2" width="8.8" height="6" fill="none" stroke="#141414" stroke-width="0.9"/><path d="M0.8 2.2 L5 5.4 L9.2 2.2" fill="none" stroke="#141414" stroke-width="0.9"/></svg>
        mlindqvist@vornettstudio.com
      </li>
      <li>
        <svg viewBox="0 0 10 10" aria-hidden="true"><circle cx="5" cy="5" r="4.4" fill="#141414"/><path d="M0.6 5 H9.4 M5 0.6 V9.4 M1.4 2.9 H8.6 M1.4 7.1 H8.6" stroke="#f7f7f5" stroke-width="0.5"/><ellipse cx="5" cy="5" rx="2" ry="4.4" fill="none" stroke="#f7f7f5" stroke-width="0.5"/></svg>
        www.vornettstudio.com
      </li>
    </ul>
  </div>
</section>

<section class="card card--back" aria-label="Card back">
  <p class="back__name">Vornett Home Design</p>
  <div class="back__field" role="img" aria-label="Large embossed company symbol in dark tones"></div>
</section>

</body>
</html>
```